First Aid Training business needs business card design

We would like a double sided business card designed for a first aid training business - Brindlewood First Aid. We provide first aid training and , WHS (work, health and safety) training.

The attached word document contains the key information we would like on each side of the business card.

Final design needs to be delivered in print ready format, along with the original file.

```html
<!DOCTYPE html>
<html lang="en">
<head>
<meta charset="utf-8">
<title>Brindlewood First Aid – Business Card</title>
<link href="https://fonts.googleapis.com/css2?family=Montserrat:wght@700&family=Open+Sans:wght@400;600&display=swap" rel="stylesheet">
<style>
  :root {
    --bg: #b0b1b0;
    --paper: #ffffff;
    --ink: #0b0b0b;
    --red: #e92128;
    --grey: #8a8a8a;
    --text-grey: #555555;
    --white: #ffffff;
  }
  * { box-sizing: border-box; margin: 0; padding: 0; }
  html, body {
    width: 1200px; height: 1200px; overflow: hidden;
    background: var(--bg);
    font-family: "Open Sans", sans-serif;
  }
  .canvas { position: relative; width: 1200px; height: 1200px; }

  .card {
    position: absolute; left: 222px; width: 755px; height: 463px; overflow: hidden;
  }
  .card--front { top: 109px; background: var(--paper); }
  .card--back { top: 629px; background: var(--ink); }

  /* brand name block */
  .brand { position: absolute; display: flex; align-items: center; gap: 18px; }
  .brand__dot { border-radius: 50%; background: var(--red); flex: none; }
  .brand__name {
    font-family: "Montserrat", sans-serif; font-weight: 700;
    text-transform: uppercase; line-height: 1.05; letter-spacing: 0.5px;
  }
  .card--front .brand { left: 45px; top: 62px; }
  .card--front .brand__dot { width: 64px; height: 64px; }
  .card--front .brand__name { font-size: 30px; color: var(--ink); }

  .card--back .brand {
    left: 0; right: 0; top: 120px; flex-direction: column; gap: 26px; text-align: center;
  }
  .card--back .brand__dot { width: 110px; height: 110px; }
  .card--back .brand__name { font-size: 44px; color: var(--white); }

  /* person */
  .person { position: absolute; right: 50px; top: 190px; text-align: right; }
  .person__name { font-size: 38px; font-weight: 600; color: var(--red); line-height: 1.1; letter-spacing: -0.3px; }
  .person__title { font-size: 22px; color: var(--text-grey); line-height: 1.3; }

  .divider { position: absolute; left: 45px; right: 50px; top: 267px; height: 3px; background: var(--ink); }

  /* contacts */
  .contacts { position: absolute; left: 45px; top: 298px; list-style: none; }
  .contacts__item {
    display: flex; align-items: center; gap: 11px;
    font-size: 21px; color: var(--text-grey); height: 31px;
  }
  .contacts__icon { width: 20px; height: 20px; flex: none; }

  .address { position: absolute; right: 50px; top: 334px; text-align: right; }
  .address__pin { width: 20px; height: 28px; display: block; margin-left: auto; margin-bottom: 6px; }
  .address__line { font-size: 20px; color: var(--text-grey); line-height: 27px; }

  .band { position: absolute; bottom: 0; height: 19px; }
  .band--red { left: 0; width: 478px; background: var(--red); }
  .band--grey { left: 478px; right: 0; background: var(--grey); }
</style>
</head>
<body>
<main class="canvas">

  <section class="card card--front" aria-label="Business card front">
    <div class="brand">
      <span class="brand__dot"></span>
      <div class="brand__name">Brindlewood<br>First Aid</div>
    </div>

    <div class="person">
      <p class="person__name">Marcus Ellery</p>
      <p class="person__title">Account Executive</p>
    </div>

    <div class="divider"></div>

    <ul class="contacts">
      <li class="contacts__item">
        <svg class="contacts__icon" viewBox="0 0 24 24" aria-hidden="true"><path fill="#e92128" d="M6.6 10.8a15.1 15.1 0 0 0 6.6 6.6l2.2-2.2a1 1 0 0 1 1-.25 11.4 11.4 0 0 0 3.6.57 1 1 0 0 1 1 1V20a1 1 0 0 1-1 1A17 17 0 0 1 3 4a1 1 0 0 1 1-1h3.5a1 1 0 0 1 1 1c0 1.25.2 2.45.57 3.57a1 1 0 0 1-.25 1z"/></svg>
        555.310.4182
      </li>
      <li class="contacts__item">
        <svg class="contacts__icon" viewBox="0 0 24 24" aria-hidden="true"><path fill="#e92128" d="M6 2h12v5H6zM3 8h18a2 2 0 0 1 2 2v7h-4v5H5v-5H1v-7a2 2 0 0 1 2-2zm4 7v5h10v-5z"/></svg>
        555.310.4190
      </li>
      <li class="contacts__item">
        <svg class="contacts__icon" viewBox="0 0 24 24" aria-hidden="true"><path fill="#e92128" d="M2 5h18v8.5a5.5 5.5 0 0 0-7 6.5H2zm1.5 1.5L11 12l7.5-5.5z"/><circle cx="18.5" cy="18.5" r="4.5" fill="#e92128"/><path d="M16.5 18.5l1.5 1.5 2.5-2.8" stroke="#fff" stroke-width="1.4" fill="none"/></svg>
        mellery@brindlewood.com
      </li>
      <li class="contacts__item">
        <svg class="contacts__icon" viewBox="0 0 24 24" aria-hidden="true"><g fill="none" stroke="#e92128" stroke-width="1.6"><circle cx="12" cy="12" r="10"/><ellipse cx="12" cy="12" rx="4.5" ry="10"/><path d="M2 12h20M4 6.5h16M4 17.5h16"/></g></svg>
        www.brindlewood.com
      </li>
    </ul>

    <div class="address">
      <svg class="address__pin" viewBox="0 0 20 28" aria-hidden="true"><path fill="#e92128" d="M10 0a10 10 0 0 0-10 10c0 7 10 18 10 18s10-11 10-18A10 10 0 0 0 10 0zm0 14a4 4 0 1 1 0-8 4 4 0 0 1 0 8z"/></svg>
      <p class="address__line">48 Harlow Street Suite 210</p>
      <p class="address__line">Fairhaven, CA 94512</p>
    </div>

    <div class="band band--red"></div>
    <div class="band band--grey"></div>
  </section>

  <section class="card card--back" aria-label="Business card back">
    <div class="brand">
      <span class="brand__dot"></span>
      <div class="brand__name">Brindlewood<br>First Aid</div>
    </div>
  </section>

</main>
</body>
</html>
```